The Heron Wand for the Company The Velvet Bayou

This vibrator is a sex toy. It will represent the brand from the Velvet Bayou which is an upcoming adult novelty wholesale company. This will be our first vibrator on the market. Looking for a cajun-southern-louisiana touch. Fun, classy, feminine, and eye catching. I am looking for packaging that will be appealing to boutique style adult novelty stores. I will attach the Velvet Bayou logo. The vibrator will have dual power options and made of high quality grade materials....which means it will be a higher end toy like the MIRVA. I have attached the logo for The Velvet Bayou which is the business name in addition to a vibrator which will be close in the style choice of our design. The Velvet Bayou is a sister company of Hold Me Silks.

Target Market(s)

Females ages 18-60. Middle class with an eye for class and style.

Industry/Entity Type

Retail

Colors
eda3c7
e667a6
e34297
b7a5cd
876aae
6b449b
ffffff
9d9d9d
1b1b1b

Requirements
Must have
• The name of the Product is "the Heron Wand" (without parenthesis)
• The name of the company is the Velvet Bayou.
• The packaging will be a see-through on the front and not see through on the back. (not sure if that is significant) but I want a catchy logo for the name in addition to a picture which corresponds to the Velvet Bayou. Colors I am not too sure about. Packaging is key and the target would include women; so extremely feminine and eye catching. CLASS, FEMININE.....
• I want all retailers to want to put this item in their store.
Nice to have
• a Gator picture incorporated with the logo. Creative flare and female driven design. Soft and elegant - fun, sexy, trendy.

```html
<!DOCTYPE html>
<html lang="en">
<head>
<meta charset="utf-8">
<title>The Heron Wand – Packaging Options</title>
<link rel="stylesheet" href="https://fonts.googleapis.com/css2?family=Bebas+Neue&family=Fredoka:wght@600&family=Open+Sans:wght@400;700;800&display=swap">
<style>
  :root {
    --page-light: #ffffff;
    --page-edge: #e4e4e4;
    --ink: #1b1b1b;
    --white: #ffffff;
    --gold: #d9a033;
    --pink-hot: #e34297;
    --pink-mid: #e667a6;
    --pink-soft: #eda3c7;
    --pink-pale: #f7d6e6;
    --pink-band: #f0c0d7;
    --pink-deep-band: #e89cc3;
    --violet: #6b449b;
    --magenta-line: #c8338a;
    --grey: #9d9d9d;
  }
  * { box-sizing: border-box; margin: 0; padding: 0; }
  html, body { width: 1200px; height: 1000px; overflow: hidden; }
  body {
    position: relative;
    background: radial-gradient(ellipse at 50% 45%, var(--page-light) 0%, #f3f3f3 55%, var(--page-edge) 100%);
    font-family: "Open Sans", sans-serif;
  }
  .package {
    position: absolute;
    top: 35px;
    width: 384px;
    height: 902px;
    border: 4px solid var(--white);
    border-radius: 38px;
    overflow: hidden;
    box-shadow: 0 2px 10px rgba(0,0,0,0.12);
  }
  .package--one {
    left: 130px;
    background: linear-gradient(160deg, #ef86b6 0%, var(--pink-mid) 35%, #dd5596 70%, #c8347f 100%);
  }
  .package--two { left: 686px; background: var(--pink-pale); }
  .package__waves { position: absolute; inset: 0; }
  .hang-tab {
    position: absolute;
    left: 121px; top: 0;
    width: 134px; height: 112px;
    background: var(--white);
    display: flex; flex-direction: column; align-items: center; justify-content: center;
    padding-top: 18px;
  }
  .hang-tab__slot {
    position: absolute;
    top: 6px; left: 50%;
    width: 34px; height: 12px;
    margin-left: -17px;
    border: 2px solid #d5d5d5;
    border-radius: 8px;
  }
  .brand-mark__dot {
    width: 14px; height: 14px; border-radius: 50%;
    background: var(--pink-soft);
    margin-bottom: 6px;
  }
  .brand-mark__name {
    font-family: "Fredoka", sans-serif;
    font-weight: 600;
    font-size: 17px;
    line-height: 1.05;
    text-align: center;
    color: var(--pink-hot);
  }
  .product-title {
    position: absolute;
    left: 0; right: 0; top: 128px;
    text-align: center;
    font-family: "Fredoka", sans-serif;
    font-weight: 600;
    line-height: 0.92;
  }
  .product-title__the { display: block; font-size: 40px; }
  .product-title__name { display: block; font-size: 64px; }
  .package--one .product-title { color: var(--gold); }
  .package--two .product-title { color: var(--violet); }
  .product-window {
    position: absolute;
    left: 23px; top: 308px;
    width: 205px; height: 640px;
    border: 4px dashed var(--white);
    border-radius: 32px 32px 0 0;
  }
  .package--two .product-window { border-color: var(--magenta-line); }
  .product-window__label {
    position: absolute;
    left: 0; right: 0; top: 240px;
    text-align: center;
    font-family: "Bebas Neue", sans-serif;
    font-size: 48px;
    line-height: 64px;
    color: var(--white);
  }
  .package--two .product-window__label { color: #c2388a; }
  .feature-column {
    position: absolute;
    left: 254px; top: 862px;
    width: 505px;
    transform: rotate(-90deg);
    transform-origin: top left;
    color: var(--white);
  }
  .package--two .feature-column { color: var(--magenta-line); }
  .feature-column__heading {
    font-weight: 800;
    font-size: 19px;
    letter-spacing: 0.5px;
    line-height: 24px;
    margin-bottom: 6px;
  }
  .feature-column__text {
    font-size: 8px;
    line-height: 11px;
    text-align: justify;
    margin-bottom: 6px;
  }
  .option-label {
    position: absolute;
    top: 952px;
    width: 384px;
    text-align: center;
    font-weight: 800;
    font-size: 20px;
    letter-spacing: 0.5px;
    color: var(--ink);
  }
  .option-label--one { left: 130px; }
  .option-label--two { left: 686px; }
</style>
</head>
<body>

<section class="package package--one" aria-label="Packaging option 1">
  <div class="hang-tab">
    <span class="hang-tab__slot"></span>
    <span class="brand-mark__dot"></span>
    <span class="brand-mark__name">The Velvet Bayou</span>
  </div>
  <h1 class="product-title">
    <span class="product-title__the">The</span>
    <span class="product-title__name">Heron</span>
    <span class="product-title__name">Wand</span>
  </h1>
  <div class="product-window"><p class="product-window__label">Product<br>Here!</p></div>
  <div class="feature-column">
    <h2 class="feature-column__heading">DUAL POWER OPTIONS</h2>
    <p class="feature-column__text">Crafted from body-safe premium silicone, the Heron Wand glides with a silky velvet finish. Choose rechargeable power or standard batteries for pleasure anywhere. Ten rhythm settings, whisper-quiet motor and a fully waterproof body make every moment feel easy, elegant and indulgent.</p>
    <p class="feature-column__text">Designed in the spirit of the bayou, made for women with style. Clean before and after each use and store in a cool dry place.</p>
  </div>
</section>

<section class="package package--two" aria-label="Packaging option 2">
  <svg class="package__waves" viewBox="0 0 376 894" preserveAspectRatio="none" aria-hidden="true">
    <path d="M0 392 C 120 330, 250 300, 376 250 L376 894 L0 894 Z" fill="var(--pink-band)"/>
    <path d="M0 820 C 150 720, 275 560, 376 420 L376 894 L0 894 Z" fill="var(--pink-deep-band)"/>
  </svg>
  <div class="hang-tab">
    <span class="hang-tab__slot"></span>
    <span class="brand-mark__dot"></span>
    <span class="brand-mark__name">The Velvet Bayou</span>
  </div>
  <h1 class="product-title">
    <span class="product-title__the">The</span>
    <span class="product-title__name">Heron</span>
    <span class="product-title__name">Wand</span>
  </h1>
  <div class="product-window"><p class="product-window__label">Product<br>Here!</p></div>
  <div class="feature-column">
    <h2 class="feature-column__heading">DUAL POWER OPTIONS</h2>
    <p class="feature-column__text">Crafted from body-safe premium silicone, the Heron Wand glides with a silky velvet finish. Choose rechargeable power or standard batteries for pleasure anywhere. Ten rhythm settings, whisper-quiet motor and a fully waterproof body make every moment feel easy, elegant and indulgent.</p>
    <p class="feature-column__text">Designed in the spirit of the bayou, made for women with style. Clean before and after each use and store in a cool dry place.</p>
  </div>
</section>

<p class="option-label option-label--one">OPTION 1</p>
<p class="option-label option-label--two">OPTION 2</p>

</body>
</html>
```